Innovation Presentation Template

I need a unique template design for a presentation on Innovation used exclusively inside of our company. I'd prefer to work in Apple Keynote but can take a .ppt and convert it. The template should appeal to a broad audience of diverse job descriptions. This is a one-time presentation that will last between 30 and 45 minutes. The design should provide a strong visual appeal with multiple chart layouts to support highlighted test points (no bullets, I hate bullets), graphics, line art, and video/photos. My presentations are sparse, never more that 2 concepts per chart (usually one). Our company is a high tech manufacturer selling products in many markets ranging from Government to consumer. The final design should include style a style guide including suggested fonts, colors, graph formats, suggested word art, etc.

Target Market(s)

The audience is internal employees only. Strong corporate branding is not required in this presentation.

Industry/Entity Type

Government

Colors
3277b5
faa54b

Requirements
Must have
• Strong visual appeal helping to support the communication of simple concepts (that have been broken down from complex subject matter).

Multiple chart template forms to support different forms of communication including text points, data charts, graphics, photos, and videos.

Visuals will be memorable, but not overpower the content. Visuals will help convey the content.

Well conceived and coordinated color pallets. Fonts guides (that I can access).

You can visit our company web site at www.vantrel-example.com to see logo and corporate look/feel. It would be good to build logo into a few of the chart templates, but not all.
Nice to have
• Keynote (please). I can live with .ppt if I have to.

Many charts will make a point with simple single sentences. Find a way to make the sentences graphically interesting by varying font and/or color of specific words to help drive points.

Note that colors that I've identified below are based upon the blue used in our logo and the orange that complements it. I'm not married to these but use them as guidelines.
Should not have
• Noise. Corporate nauseia.

```html
<!DOCTYPE html>
<html lang="en">
<head>
<meta charset="utf-8">
<title>Project Title Here</title>
<link rel="stylesheet" href="https://fonts.googleapis.com/css2?family=Archivo+Black&family=Arimo:wght@400;700&display=swap">
<style>
  :root {
    --brand-blue: #3277b5;
    --bright-blue: #1f80d8;
    --brand-orange: #faa54b;
    --slate: #555555;
    --stone: #808080;
    --mist: #c2c2c2;
    --ink: #111111;
    --paper: #ffffff;
    --paper-shade: #eef1f4;
  }
  * { margin: 0; padding: 0; box-sizing: border-box; }
  html, body { width: 1200px; height: 900px; overflow: hidden; background: var(--paper); }
  .slide {
    position: relative;
    width: 1200px;
    height: 900px;
    overflow: hidden;
    background: radial-gradient(ellipse at 60% 45%, var(--paper) 30%, var(--paper-shade) 100%);
    font-family: "Arimo", Arial, sans-serif;
  }
  .frame { position: absolute; left: 0; width: 1200px; }
  .frame--top { top: 0; height: 140px; }
  .frame--bottom { bottom: 0; height: 160px; }
  .slide-title {
    position: absolute;
    left: 52px;
    top: 24px;
    font-family: "Archivo Black", "Arial Black", sans-serif;
    font-size: 36px;
    line-height: 44px;
    letter-spacing: 0.3px;
    color: var(--paper);
    font-weight: 400;
    z-index: 2;
  }
  .content {
    position: absolute;
    left: 55px;
    top: 224px;
    width: 518px;
  }
  .content-heading {
    font-size: 31px;
    font-weight: 700;
    color: var(--brand-blue);
    margin-bottom: 20px;
  }
  .content-text {
    font-size: 18.5px;
    line-height: 33px;
    color: var(--ink);
    text-align: justify;
    text-align-last: left;
    margin-bottom: 33px;
  }
  .pie-chart { position: absolute; left: 670px; top: 206px; width: 490px; height: 480px; }
  .pie-label { font-family: "Arimo", Arial, sans-serif; font-size: 16px; font-weight: 700; }
  .pie-label--dark { fill: var(--ink); }
  .pie-label--light { fill: var(--paper); }
  .brand-mark {
    position: absolute;
    left: 114px;
    top: 768px;
    display: flex;
    align-items: center;
    gap: 12px;
  }
  .brand-mark__square { width: 44px; height: 44px; background: var(--brand-blue); }
  .brand-mark__name {
    font-family: "Arimo", Arial, sans-serif;
    font-weight: 700;
    font-size: 50px;
    color: var(--brand-blue);
    letter-spacing: 1px;
  }
</style>
</head>
<body>
<div class="slide">
  <svg class="frame frame--top" viewBox="0 0 1200 140" aria-hidden="true">
    <path d="M0,0 H1200 V28 C1000,26 820,30 700,48 C560,70 420,96 0,92 Z" fill="var(--brand-blue)"/>
    <path d="M0,104 C420,108 560,82 700,60 C820,42 1000,38 1200,40 V52 C1000,50 820,54 700,72 C560,94 420,120 0,116 Z" fill="var(--brand-orange)"/>
  </svg>
  <h1 class="slide-title">PROJECT TITLE HERE</h1>

  <section class="content">
    <h2 class="content-heading">Lorem ipsum dolor sit ipsum</h2>
    <p class="content-text">Lorem ipsum dolor sit ipsum Lorem ipsum dolor sit ipsum Lorem ipsum dolor sit ipsum Lorem ipsum dolor sit ipsum lorem ipsum dolor sit ipsum Lorem ipsum dolor sit ipsum Lorem ipsum dolor sit ipsum</p>
    <p class="content-text">Lorem ipsum dolor sit ipsum Lorem ipsum dolor sit ipsum Lorem ipsum dolor sit ipsum Lorem ipsum dolor sit ipsum</p>
    <p class="content-text">Lorem ipsum dolor sit ipsum Lorem ipsum dolor sit ipsum Lorem ipsum dolor sit ipsum Lorem ipsum dolor sit ipsum lorem ipsum dolor sit ipsum Lorem ipsum dolor sit ipsum Lorem ipsum dolor sit ipsum</p>
  </section>

  <svg class="pie-chart" viewBox="670 206 490 480" role="img" aria-label="Pie chart with six segments">
    <g stroke="var(--paper)" stroke-width="2" stroke-linejoin="round">
      <path d="M911,446 L911,216 A230,230 0 0 1 1043,258 Z" fill="var(--mist)"/>
      <path d="M911,446 L1043,258 A230,230 0 0 1 1128.5,521 Z" fill="var(--brand-orange)"/>
      <path d="M911,446 L1128.5,521 A230,230 0 0 1 993,661 Z" fill="var(--bright-blue)"/>
      <path d="M911,446 L993,661 A230,230 0 0 1 695,525 Z" fill="var(--brand-blue)"/>
      <path d="M911,446 L695,525 A230,230 0 0 1 782,255 Z" fill="var(--slate)"/>
      <path d="M911,446 L782,255 A230,230 0 0 1 911,216 Z" fill="var(--stone)"/>
    </g>
    <circle cx="911" cy="446" r="36" fill="var(--paper)" stroke="var(--brand-orange)" stroke-width="5"/>
    <text class="pie-label pie-label--dark" text-anchor="middle">
      <tspan x="957" y="280">Lorem</tspan><tspan x="957" y="305">ipsum</tspan><tspan x="957" y="330">dolor</tspan>
    </text>
    <text class="pie-label pie-label--light" text-anchor="middle">
      <tspan x="867" y="280">Lorem</tspan><tspan x="867" y="305">ipsum</tspan><tspan x="867" y="330">dolor</tspan>
    </text>
    <text class="pie-label pie-label--dark" text-anchor="middle">
      <tspan x="1052" y="413">Lorem ipsum</tspan><tspan x="1052" y="438">dolor</tspan>
    </text>
    <text class="pie-label pie-label--dark" text-anchor="middle">
      <tspan x="1023" y="540">Lorem ipsum</tspan><tspan x="1023" y="564">dolor</tspan>
    </text>
    <text class="pie-label pie-label--dark" text-anchor="middle">
      <tspan x="847" y="553">Lorem ipsum dolor</tspan><tspan x="847" y="578">Lorem ipsum dolor</tspan>
    </text>
    <text class="pie-label pie-label--light" text-anchor="middle">
      <tspan x="782" y="406">Lorem ipsum dolor</tspan><tspan x="782" y="430">Lorem ipsum dolor</tspan>
    </text>
  </svg>

  <svg class="frame frame--bottom" viewBox="0 0 1200 160" aria-hidden="true">
    <path d="M0,114 C260,132 520,64 760,40 C940,22 1080,28 1200,40 V52 C1080,40 940,36 760,54 C520,78 260,146 0,128 Z" fill="var(--brand-orange)"/>
    <path d="M0,136 C260,154 520,86 760,62 C940,44 1080,48 1200,60 V160 H0 Z" fill="var(--brand-blue)"/>
  </svg>

  <div class="brand-mark">
    <span class="brand-mark__square" aria-hidden="true"></span>
    <span class="brand-mark__name">VANTREL</span>
  </div>
</div>
</body>
</html>
```